Business Card Design Project

i need a bussines car design
Velora Clinical Hypnotherapy

Daniel Herwood
Psychotherapy & Hypnosis

94265831 /0417529046

back of the card appoinment space.

file was provided on a PDF, LOgo , use the blu colorsa as well , elegant, clear,

Target Market(s)

young professional, caucasian , young mothers.

Industry/Entity Type

Business

```html
<!DOCTYPE html>
<html lang="en">
<head>
<meta charset="utf-8">
<title>Velora Clinical Hypnotherapy – Business Card</title>
<link href="https://fonts.googleapis.com/css2?family=Arvo:wght@400;700&display=swap" rel="stylesheet">
<style>
  :root {
    --page: #e9e9ea;
    --card: #f3f3f3;
    --blue: #2d6cb3;
    --blue-light: #7fb0dc;
    --ink: #1c1c1c;
    --muted: #555;
    --photo-top: #e7d9cc;
    --photo-bottom: #d8bfa9;
  }
  * { box-sizing: border-box; margin: 0; padding: 0; }
  html, body { width: 1200px; height: 800px; overflow: hidden; }
  body {
    background: var(--page);
    font-family: "Arvo", Georgia, serif;
    color: var(--ink);
    position: relative;
  }
  .card {
    position: absolute;
    top: 245px;
    width: 525px;
    height: 300px;
    background: var(--card);
    box-shadow: 0 6px 18px rgba(0,0,0,0.12);
    overflow: hidden;
  }
  .card--front { left: 45px; }
  .card--back  { left: 630px; }

  /* front */
  .brand {
    position: absolute; left: 40px; top: 70px;
    display: flex; flex-direction: column;
  }
  .brand__row { display: flex; align-items: center; gap: 10px; }
  .brand__dot { width: 22px; height: 22px; border-radius: 50%; background: var(--blue); }
  .brand__name { font-size: 22px; color: var(--blue); font-weight: 400; letter-spacing: 0.3px; }
  .brand__url { font-size: 9px; color: var(--muted); margin: 4px 0 0 32px; letter-spacing: 0.6px; }

  .photo {
    position: absolute; right: 0; top: 0;
    width: 210px; height: 190px;
    background: linear-gradient(180deg, var(--photo-top), var(--photo-bottom));
  }

  .person { position: absolute; left: 40px; top: 170px; }
  .person__marker {
    position: absolute; left: -22px; top: 4px;
    width: 0; height: 0;
    border-top: 7px solid transparent; border-bottom: 7px solid transparent;
    border-left: 11px solid var(--blue);
  }
  .person__name { font-size: 17px; font-weight: 700; color: var(--blue); }
  .person__role { font-size: 9.5px; font-weight: 700; margin-top: 1px; }

  .contact { list-style: none; position: absolute; left: 40px; top: 218px; }
  .contact li { display: flex; align-items: center; gap: 8px; font-size: 10.5px; font-weight: 700; line-height: 17px; }
  .contact svg { width: 12px; height: 12px; flex: none; }

  /* back */
  .appointments { position: absolute; left: 40px; top: 48px; }
  .appointments__title { font-size: 15px; font-weight: 700; color: var(--blue); margin-bottom: 10px; }
  .appointments ol { list-style: none; }
  .appointments li {
    display: flex; align-items: flex-end; gap: 6px;
    font-size: 11px; color: var(--blue); height: 24px;
  }
  .appointments .num { width: 14px; color: var(--ink); }
  .line { border-bottom: 1px solid var(--blue); height: 12px; }
  .line--time { width: 40px; }
  .line--day { width: 150px; margin-left: 6px; }
  .line--date { width: 22px; }

  .notice {
    position: absolute; left: 40px; bottom: 34px;
    font-size: 8.5px; line-height: 13px; color: var(--blue); max-width: 330px;
  }
  .notice__reg { margin-top: 4px; font-size: 7.5px; }
</style>
</head>
<body>

<section class="card card--front" aria-label="Business card front">
  <div class="brand">
    <div class="brand__row">
      <span class="brand__dot"></span>
      <span class="brand__name">Velora Hypnotherapy</span>
    </div>
    <span class="brand__url">www.veloraclinicalhypnotherapy.com.au</span>
  </div>

  <div class="photo" role="img" aria-label="Portrait photograph of Daniel Herwood"></div>

  <div class="person">
    <span class="person__marker"></span>
    <p class="person__name">Daniel Herwood</p>
    <p class="person__role">Psychotherapy &amp; Hypnosis</p>
  </div>

  <ul class="contact">
    <li>
      <svg viewBox="0 0 12 12" aria-hidden="true"><rect width="12" height="12" rx="2" fill="#2d6cb3"/><path d="M3.5 3h1.5l.7 1.6-.9.7a4.5 4.5 0 0 0 1.9 1.9l.7-.9 1.6.7V8.5c0 .3-.3.5-.6.5A5.5 5.5 0 0 1 3 3.6c0-.3.2-.6.5-.6z" fill="#fff"/></svg>
      94265831 / 0417529046
    </li>
    <li>
      <svg viewBox="0 0 12 12" aria-hidden="true"><rect width="12" height="12" rx="2" fill="#2d6cb3"/><rect x="2.5" y="3.5" width="7" height="5" fill="none" stroke="#fff" stroke-width="0.9"/><path d="M2.5 3.5 6 6.5l3.5-3" fill="none" stroke="#fff" stroke-width="0.9"/></svg>
      info@veloraclinicaltherapy.com.au
    </li>
    <li>
      <svg viewBox="0 0 12 12" aria-hidden="true"><rect width="12" height="12" rx="2" fill="#2d6cb3"/><circle cx="6" cy="6" r="3.3" fill="none" stroke="#fff" stroke-width="0.9"/><path d="M2.7 6h6.6M6 2.7c-1.4 1.8-1.4 4.8 0 6.6M6 2.7c1.4 1.8 1.4 4.8 0 6.6" fill="none" stroke="#fff" stroke-width="0.7"/></svg>
      www.veloraclinicaltherapy.com.au
    </li>
  </ul>
</section>

<section class="card card--back" aria-label="Business card back">
  <div class="appointments">
    <h2 class="appointments__title">Your Appointments</h2>
    <ol>
      <li><span class="num">1.</span><span class="line line--time"></span>am/pm<span class="line line--day"></span><span class="line line--date"></span>/<span class="line line--date"></span>/<span class="line line--date"></span></li>
      <li><span class="num">2.</span><span class="line line--time"></span>am/pm<span class="line line--day"></span><span class="line line--date"></span>/<span class="line line--date"></span>/<span class="line line--date"></span></li>
      <li><span class="num">3.</span><span class="line line--time"></span>am/pm<span class="line line--day"></span><span class="line line--date"></span>/<span class="line line--date"></span>/<span class="line line--date"></span></li>
      <li><span class="num">4.</span><span class="line line--time"></span>am/pm<span class="line line--day"></span><span class="line line--date"></span>/<span class="line line--date"></span>/<span class="line line--date"></span></li>
      <li><span class="num">5.</span><span class="line line--time"></span>am/pm<span class="line line--day"></span><span class="line line--date"></span>/<span class="line line--date"></span>/<span class="line line--date"></span></li>
    </ol>
  </div>

  <div class="notice">
    <p>To reschedule your appointment please SMS or call 0417 529 046 at least 24 hours prior to your allocated time. Thank you.</p>
    <p class="notice__reg">NHRA Registration No. NP5290417</p>
  </div>
</section>

</body>
</html>
```